Business Card Design

- one on one personal training
- group personal training
- indoor or outdoor training available
- fitness and health assessments
- personalised fitness programs
- flexible hours for training

I am a Personal Trainer in Perth Australia. I am looking to expand my word of mouth client base.

I would like to see something that uses the colours blue, green and/or yellow.

The final design should reflect the way that I train clients, fun, motivating and perhaps a little quirky?
Updates

update with a logo with the letters MPT thank you

Hi all, Have had some great designs so far. Have decided to go double sided, perhaps to use the back to list my services. Thank you

Please check update brief. Thank you.

Target Market(s)

Professionals, ages 30 to 60

Industry/Entity Type

Training

Contact Information for Business Card

Mandy Whitlock
Personal Trainer

0471 208 514
mandypersonaltrainer@fitmailbox.example
http://www.mandypersonaltrainer.example

Requirements
Must have
• A logo with the letter MPT
Nice to have
• a logo to represent either; fitness, health, change, overall well-being.
Should not have
• Please no weights or lotus flowers!!

```html
<!DOCTYPE html>
<html lang="en">
<head>
<meta charset="utf-8">
<title>MPT Personal Training – Business Card</title>
<link rel="stylesheet" href="https://fonts.googleapis.com/css2?family=Bebas+Neue&family=Open+Sans:wght@400;600&display=swap">
<style>
  :root {
    --stage: #3a3a3a;
    --card-black: #0d0d0d;
    --card-black-soft: #1e1e1e;
    --gold: #d9b21c;
    --gold-light: #f6e04a;
    --gold-deep: #a8840c;
    --service-yellow: #f3ea2c;
    --paper: #f4f4f4;
    --paper-shade: #e2e2e2;
    --ink: #1a1a1a;
    --name-gold: #c9a227;
  }
  * { margin: 0; padding: 0; box-sizing: border-box; }
  html, body { width: 1200px; height: 750px; overflow: hidden; }
  body {
    background: var(--stage);
    position: relative;
    font-family: "Open Sans", sans-serif;
  }
  .card {
    position: absolute;
    top: 211px;
    width: 511px;
    height: 293px;
    border-radius: 18px;
    overflow: hidden;
  }
  .card--front { left: 78px; background: var(--paper); }
  .card--back {
    left: 609px;
    background: radial-gradient(ellipse at 50% 40%, var(--card-black-soft), var(--card-black) 75%);
  }

  /* front: upper black panel */
  .front-panel {
    position: absolute;
    left: 0; top: 0;
    width: 100%; height: 174px;
    background: radial-gradient(ellipse at 50% 30%, var(--card-black-soft), var(--card-black) 80%);
  }
  .brand-name {
    position: absolute;
    left: 0; right: 0; top: 60px;
    text-align: center;
    font-family: "Open Sans", sans-serif;
    font-weight: 600;
    font-size: 46px;
    line-height: 1;
    color: var(--gold);
  }
  .gold-band {
    position: absolute;
    left: 0; top: 174px;
    width: 100%; height: 13px;
    background: linear-gradient(180deg, var(--gold-light), var(--gold) 55%, var(--gold-deep));
    border-bottom: 2px solid var(--card-black);
  }
  .front-info {
    position: absolute;
    left: 0; top: 189px;
    width: 100%; height: 104px;
    background: linear-gradient(120deg, var(--paper) 0%, #ffffff 40%, var(--paper-shade) 100%);
  }
  .trainer {
    position: absolute;
    left: 33px; top: 20px;
  }
  .trainer__name {
    font-size: 17px;
    color: var(--name-gold);
    line-height: 1.2;
  }
  .trainer__role {
    font-size: 13.5px;
    color: var(--ink);
    margin-top: 1px;
  }
  .contacts {
    position: absolute;
    left: 216px; top: 17px;
    list-style: none;
  }
  .contacts__item {
    display: flex;
    align-items: center;
    height: 18px;
    font-size: 12.8px;
    color: var(--ink);
    white-space: nowrap;
  }
  .contacts__icon {
    width: 13px; height: 13px;
    margin-right: 8px;
    flex: none;
  }

  /* back */
  .back-glow {
    position: absolute;
    left: 85px; top: 42px;
    width: 337px; height: 206px;
    background: radial-gradient(ellipse at 50% 55%, rgba(217, 178, 28, 0.14), rgba(217, 178, 28, 0.04) 60%, transparent 80%);
  }
  .services {
    position: absolute;
    left: 0; right: 0; top: 81px;
    list-style: none;
    text-align: center;
    font-family: "Bebas Neue", sans-serif;
    font-size: 23px;
    line-height: 21.3px;
    color: var(--service-yellow);
    letter-spacing: 0.2px;
  }
</style>
</head>
<body>

  <section class="card card--front" aria-label="Business card front">
    <div class="front-panel">
      <p class="brand-name">MPT</p>
    </div>
    <div class="gold-band"></div>
    <div class="front-info">
      <div class="trainer">
        <p class="trainer__name">Mandy Whitlock</p>
        <p class="trainer__role">Personal Trainer</p>
      </div>
      <ul class="contacts">
        <li class="contacts__item">
          <svg class="contacts__icon" viewBox="0 0 16 16" aria-hidden="true">
            <path fill="var(--gold)" d="M2 5c0-2 2-3 6-3s6 1 6 3v1h-3V5H5v1H2zM4 8l2-2h4l2 2 2 5H2z"/>
            <circle cx="8" cy="10" r="1.6" fill="var(--paper)"/>
          </svg>
          0471 208 514
        </li>
        <li class="contacts__item">
          <svg class="contacts__icon" viewBox="0 0 16 16" aria-hidden="true">
            <rect x="1" y="3" width="14" height="10" fill="var(--gold)"/>
            <path d="M1 3l7 6 7-6" fill="none" stroke="var(--paper)" stroke-width="1.3"/>
          </svg>
          mandypersonaltrainer@fitmailbox.example
        </li>
        <li class="contacts__item">
          <svg class="contacts__icon" viewBox="0 0 16 16" aria-hidden="true">
            <g fill="none" stroke="var(--gold)" stroke-width="1.2">
              <circle cx="8" cy="8" r="6.5"/>
              <ellipse cx="8" cy="8" rx="2.8" ry="6.5"/>
              <path d="M1.5 8h13M2.6 4.5h10.8M2.6 11.5h10.8"/>
            </g>
          </svg>
          www.mandypersonaltrainer.example
        </li>
      </ul>
    </div>
  </section>

  <section class="card card--back" aria-label="Business card back">
    <div class="back-glow" role="img" aria-label="Faint background decoration behind the list of services"></div>
    <ul class="services">
      <li>One on one personal training</li>
      <li>Group personal training</li>
      <li>Indoor or outdoor training available</li>
      <li>Fitness and health assessments</li>
      <li>Personalised fitness programs</li>
      <li>Flexible hours for training</li>
    </ul>
  </section>

</body>
</html>
```